We are a used car dealership that specializes in subprime financing. We we would like to have a flyer that we be more business to business. Bright Lane Motor Sales offers a $100 referral fee to other salesmen that send us leads. $100 only good on customers that purchase a vehicle. Our website is brightlanemotor.com phone 256-418-7293

```html
<!DOCTYPE html>
<html lang="en">
<head>
<meta charset="utf-8">
<title>Bright Lane Motor Sales – Referral Flyer</title>
<link rel="stylesheet" href="https://fonts.googleapis.com/css2?family=Open+Sans:wght@400;600;700;800&family=Montserrat:wght@500;600;700&display=swap">
<style>
  :root {
    --page-bg: #e4e2df;
    --paper: #f6f7f8;
    --paper-grey: #e3e6ea;
    --navy: #1b4a8f;
    --blue: #1f6db3;
    --blue-bright: #2b7fcc;
    --ink: #2b2f36;
    --rule: #6d7380;
    --white: #ffffff;
  }
  * { box-sizing: border-box; margin: 0; padding: 0; }
  html, body {
    width: 1200px; height: 1200px; overflow: hidden;
    background: var(--page-bg);
  }
  .flyer {
    position: absolute; left: 150px; top: 18px;
    width: 900px; height: 1165px;
    background: linear-gradient(180deg, var(--paper) 0%, var(--paper-grey) 70%, var(--paper) 100%);
    overflow: hidden;
    font-family: "Open Sans", Arial, sans-serif;
    color: var(--ink);
  }
  .hero-band { position: absolute; left: 0; top: 0; width: 900px; height: 820px; }
  .brand-name {
    position: absolute; left: 34px; top: 70px; width: 240px;
    font-weight: 800; font-size: 30px; line-height: 1.05;
    color: var(--navy);
  }
  .mascot-art {
    position: absolute; left: 520px; top: 34px; width: 366px; height: 720px;
    border-radius: 180px 180px 60px 60px;
    background: radial-gradient(ellipse at 50% 35%, #ffffff 0%, #c9d6e6 45%, #3f7fc4 80%, #2a5fa8 100%);
  }
  .vehicle-photo {
    position: absolute; left: 40px; top: 486px; width: 500px; height: 292px;
    border-radius: 60px 90px 20px 20px;
    background: linear-gradient(180deg, #9aa0a8 0%, #5f656d 55%, #2f3338 100%);
  }
  .headline {
    position: absolute; left: 32px; top: 318px;
    font-weight: 800; font-size: 56px; line-height: 1.04;
    color: var(--white); letter-spacing: -0.5px;
  }
  .offer {
    position: absolute; height: 116px;
    color: var(--white); text-align: center;
    font-family: "Montserrat", Arial, sans-serif;
  }
  .offer--salesmen { left: 42px; width: 440px; top: 806px; background: var(--navy);
    clip-path: polygon(0 0, 94% 0, 100% 14%, 100% 86%, 94% 100%, 0 100%); }
  .offer--customers { left: 464px; width: 428px; top: 798px; background: var(--blue);
    clip-path: polygon(5% 0, 100% 0, 100% 100%, 5% 100%, 0 86%, 0 14%); }
  .offer-amount {
    display: block; font-family: "Open Sans", Arial, sans-serif;
    font-weight: 700; font-size: 48px; line-height: 1; margin-top: 10px;
  }
  .offer-note {
    display: block; font-weight: 600; font-size: 15px; line-height: 1.35;
    letter-spacing: 0.5px; margin-top: 8px; text-transform: uppercase;
  }
  .forms {
    position: absolute; left: 46px; top: 928px; width: 846px; height: 100px;
    background: var(--white); display: flex;
  }
  .form-block { flex: 1; padding: 8px 10px 0; }
  .form-block + .form-block { border-left: 1px solid var(--rule); }
  .form-title {
    text-align: center; font-weight: 700; font-style: italic; font-size: 17px;
    color: var(--blue-bright); text-decoration: underline; margin-bottom: 4px;
  }
  .form-row { display: flex; gap: 8px; margin-top: 10px; font-size: 12px; }
  .form-field { flex: 1; display: flex; align-items: flex-end; gap: 3px; }
  .form-field span.line { flex: 1; border-bottom: 1px solid var(--rule); height: 12px; }
  .footer-band { position: absolute; left: 0; bottom: 0; width: 900px; height: 120px; }
  .contact { position: absolute; left: 28px; bottom: 24px; color: var(--white); }
  .contact-phone {
    display: flex; align-items: center; gap: 6px;
    font-weight: 700; font-size: 34px; line-height: 1;
  }
  .contact-web {
    display: flex; align-items: center; gap: 6px; margin-top: 4px;
    font-weight: 600; font-size: 22px;
  }
</style>
</head>
<body>
  <main class="flyer">
    <svg class="hero-band" viewBox="0 0 900 820" aria-hidden="true">
      <path d="M0 290 C 160 160, 380 120, 560 130 C 760 140, 900 160, 900 170 L 900 520 C 760 600, 520 650, 300 640 C 130 632, 30 590, 0 560 Z" fill="#ffffff"/>
      <path d="M0 300 C 160 175, 380 140, 560 148 C 740 156, 880 175, 900 185 L 900 505 C 760 585, 520 630, 300 622 C 130 615, 30 578, 0 548 Z" fill="var(--navy)"/>
      <path d="M540 150 C 720 158, 870 180, 900 190 L 900 500 C 820 545, 700 575, 580 595 Z" fill="var(--blue)" opacity="0.55"/>
    </svg>

    <div class="brand-name">Bright Lane Motor Sales</div>

    <div class="mascot-art" role="img" aria-label="Friendly blue and white robot mascot giving a thumbs up"></div>
    <div class="vehicle-photo" role="img" aria-label="Silver compact SUV, front three-quarter view"></div>

    <h1 class="headline">WE FINANCE<br>YOUR FUTURE</h1>

    <div class="offer offer--salesmen">
      <span class="offer-amount">$100</span>
      <span class="offer-note">Referral fee to other salesmen<br>that send us leads</span>
    </div>
    <div class="offer offer--customers">
      <span class="offer-amount">$100</span>
      <span class="offer-note">Good on customers that purchase<br>a vehicle</span>
    </div>

    <section class="forms">
      <div class="form-block">
        <h2 class="form-title">NEW CUSTOMER</h2>
        <div class="form-row">
          <div class="form-field">Name <span class="line"></span></div>
          <div class="form-field">Address <span class="line"></span></div>
        </div>
        <div class="form-row">
          <div class="form-field">Telephone <span class="line"></span></div>
          <div class="form-field">Email <span class="line"></span></div>
        </div>
      </div>
      <div class="form-block">
        <h2 class="form-title">REFERRED BY</h2>
        <div class="form-row">
          <div class="form-field">Name <span class="line"></span></div>
          <div class="form-field">Address <span class="line"></span></div>
        </div>
        <div class="form-row">
          <div class="form-field">Telephone <span class="line"></span></div>
          <div class="form-field">Email <span class="line"></span></div>
        </div>
      </div>
    </section>

    <svg class="footer-band" viewBox="0 0 900 120" aria-hidden="true">
      <path d="M0 20 C 200 0, 400 20, 580 120 L 0 120 Z" fill="var(--navy)"/>
      <path d="M150 8 C 330 6, 440 50, 520 120 L 505 120 C 430 55, 320 16, 150 8 Z" fill="var(--blue-bright)"/>
    </svg>

    <div class="contact">
      <div class="contact-phone">
        <svg width="16" height="28" viewBox="0 0 16 28" aria-hidden="true"><rect x="1.5" y="1.5" width="13" height="25" rx="2.5" fill="none" stroke="#fff" stroke-width="2.5"/></svg>
        256-418-7293
      </div>
      <div class="contact-web">
        <svg width="14" height="14" viewBox="0 0 14 14" aria-hidden="true"><circle cx="7" cy="7" r="6" fill="none" stroke="#fff" stroke-width="1.5"/><path d="M1 7h12M7 1c-3 3-3 9 0 12M7 1c3 3 3 9 0 12" fill="none" stroke="#fff" stroke-width="1.2"/></svg>
        brightlanemotor.com
      </div>
    </div>
  </main>
</body>
</html>
```